Webdesign für Naturheilpraktiker gesucht
Zielgruppe
Ich arbeite im Gesundheitswesen als Naturheilpraktiker Traditionell Tibetische Medizin.
Verfüge aber über verschiedene Anwendungstechniken.
Die Zielgruppe sind alle Menschen die mehr als nur klassische Medizin wollen, die mit der klassischen Schulmedizin nicht mehr weiter kommen und einen alternativen Weg suchen. Menschen die neben der Schulmedizin noch einen anderen Weg suchen.
Menschen im Wellness und Fitnessbereich.
Ernährungsbewusste Menschen.
Sportler allgemein da ich über eine neue Technik verfüge (KORELA) die erst auf den Markt kommt und mit der verschiedene Beschwerden gelindert werden können.
Grob gesagt alles was mit Medizin, Komplementärmedizin, Gesundheit, Wellness, Sport usw zu tun hat.
Kompetenzen der Traditionell Tibetische Medizin:
- Massage als Gesundheitssystem oder als Wellness
- Ernährungsberatung
- tibetisches Yoga
- Lebensberatung
- Familienstellen
Aufgabenstellung
Der Firmennamen und das Logo bestehen.
In der Tradition der tibetischen Medizin ist vor allem Blau (Medizin Buddha) die Farben sind aber frei wählbar.
Es soll Vertrautheit, Geborgenheit und Wärme ausstrahlen.
Nicht zu feminin erscheinen.
Einfach ein paar Ideen
http://massagepraxis-holzner-beispiel.ch
http://www.bergheilkunde-beispiel.ch

```html
<!DOCTYPE html>
<html lang="de">
<head>
<meta charset="utf-8">
<title>Über mich – LUMENSTILLE</title>
<link href="https://fonts.googleapis.com/css2?family=Open+Sans:wght@300;400;600;700&family=Josefin+Sans:wght@400&display=swap" rel="stylesheet">
<style>
  :root{
    --blue:#1f5a99;
    --blue-dark:#1d4f8c;
    --green:#2bb08a;
    --text:#555a60;
    --heading:#3d4248;
    --band:#e9eaef;
    --footer:#4d4d4d;
    --white:#ffffff;
  }
  *{margin:0;padding:0;box-sizing:border-box}
  html,body{width:891px;height:1200px;overflow:hidden;background:var(--white)}
  body{position:relative;font-family:"Open Sans",sans-serif;color:var(--text)}
  .abs{position:absolute}

  /* Hero */
  .hero{left:0;top:0;width:891px;height:182px;
    background:linear-gradient(180deg,#cfd6dc 0%,#d9dcd6 45%,#e4dcc4 62%,#c9dbe6 82%,#e6e8e4 100%)}
  .hero::after{content:"";position:absolute;inset:0;background:rgba(255,255,255,.45)}
  .brand{left:174px;top:48px;display:flex;align-items:center;gap:5px;z-index:2}
  .brand-dot{width:10px;height:10px;border-radius:50%;background:var(--blue)}
  .brand-name{font-weight:600;font-size:9px;letter-spacing:2.2px;color:var(--blue)}
  .nav{left:471px;top:36px;display:flex;gap:14.5px;z-index:2;
    font-family:"Josefin Sans",sans-serif;font-size:5.4px;letter-spacing:.3px;color:#3d4248}
  .page-title{left:0;width:891px;top:115px;text-align:center;z-index:2;
    font-weight:600;font-size:19.5px;color:var(--heading)}
  .ornament{left:418px;top:146px;z-index:2}

  /* Intro */
  .portrait{left:174px;top:210px;width:118px;height:141px;
    background:linear-gradient(180deg,#f3f3f3 0%,#ececec 60%,#e9d8cc 100%);border-bottom:1px solid var(--green)}
  .caption{left:174px;top:357px;font-size:6.2px;line-height:9.4px}
  .caption strong{font-weight:700;color:var(--heading)}
  .text{font-size:6.2px;line-height:9.4px}
  .text p+p{margin-top:9.4px}
  .text strong{font-weight:700;color:var(--heading)}
  .intro-text{left:316px;top:211px;width:400px}

  /* Timeline */
  .cv-heading{left:174px;top:393px;font-weight:400;font-size:14px;color:var(--blue)}
  .timeline-line{left:183.5px;top:441px;width:1px;height:330px;background:#c9ccd2}
  .cv-item{left:174px;width:257px}
  .cv-icon{position:absolute;left:0;top:0;width:20px;height:20px;border-radius:50%;
    border:1.6px solid var(--green);background:var(--white);display:flex;align-items:center;justify-content:center}
  .cv-date{margin-left:34px;font-weight:300;font-size:10px;color:var(--blue);line-height:12px}
  .cv-desc{margin-left:34px;margin-top:4px;font-size:6.2px;line-height:9.4px}

  /* Right column */
  .side-text-top{left:457px;top:405px;width:259px}
  .slider{left:457px;top:520px;width:259px;height:183px;
    background:linear-gradient(135deg,#cfd9c0 0%,#b98a62 40%,#d49a66 70%,#e9e4dc 100%)}
  .dots{position:absolute;left:114px;bottom:10px;display:flex;gap:5px;align-items:center}
  .dots span{width:3px;height:3px;border-radius:50%;background:var(--white)}
  .dots span.active{width:5px;height:5px;background:none;border:1px solid var(--white)}
  .side-text-bottom{left:457px;top:725px;width:262px}

  /* Contact band */
  .band{left:0;top:847px;width:891px;height:189px;background:var(--band)}
  .band-mark{left:197px;top:886px;width:118px;height:118px;border-radius:50%;
    border:6px solid var(--blue);display:flex;align-items:center;justify-content:center}
  .band-mark span{font-weight:600;font-size:10px;letter-spacing:1px;color:var(--blue)}
  .band-text{left:362px;top:904px;width:355px}
  .band-text .lead{font-weight:700;color:var(--heading);margin-bottom:9.4px}
  .cta{left:362px;top:974px;width:105px;height:18px;border-radius:9px;background:var(--blue-dark);
    color:var(--white);font-size:5.6px;display:flex;align-items:center;justify-content:center;gap:3px}

  /* Footer */
  .footer{left:0;top:1036px;width:891px;height:164px;background:var(--footer)}
  .footer-brand{left:0;width:891px;top:1082px;text-align:center;
    font-weight:600;font-size:9px;letter-spacing:2.2px;color:#d8d8d8}
  .social{left:379px;top:1127px;display:flex;gap:6px}
  .social span{width:22px;height:22px;border-radius:50%;background:var(--white)}
  .copyright{left:0;width:891px;top:1170px;text-align:center;font-size:5.8px;color:#6e6e6e}
  .to-top{left:859px;top:1158px;width:22px;height:22px;border:1px solid var(--white);
    display:flex;align-items:center;justify-content:center}
</style>
</head>
<body>

<header>
  <div class="abs hero" role="img" aria-label="Bergsee mit Gipfeln und Nadelwald im Morgenlicht, aufgehellt"></div>
  <div class="abs brand"><span class="brand-dot"></span><span class="brand-name">LUMENSTILLE</span></div>
  <nav class="abs nav">
    <span>HOME</span><span>ÜBER MICH</span><span>TIBETISCHE MEDIZIN</span><span>ANGEBOT</span><span>TERMINE</span><span>KONTAKT</span>
  </nav>
  <h1 class="abs page-title">Über mich</h1>
  <svg class="abs ornament" width="55" height="12" viewBox="0 0 55 12" aria-hidden="true">
    <line x1="0" y1="6" x2="17" y2="6" stroke="#2bb08a" stroke-width="1"/>
    <line x1="38" y1="6" x2="55" y2="6" stroke="#2bb08a" stroke-width="1"/>
    <circle cx="27.5" cy="6" r="4.5" fill="none" stroke="#2bb08a" stroke-width="1"/>
    <circle cx="27.5" cy="6" r="1.6" fill="#2bb08a"/>
  </svg>
</header>

<main>
  <div class="abs portrait" role="img" aria-label="Porträt des Praxisinhabers im weißen Hemd"></div>
  <div class="abs caption"><strong>Mustermann</strong><br>Muster Text lorem ipsum</div>

  <div class="abs text intro-text">
    <p><strong>Muster Text Lorem ipsum dolor sit amet</strong>, consetetur sadipscing elitr, sed diam nonumy eirmod tempor invidunt ut labore et dolore magna aliquyam erat, sed diam voluptua. At vero eos et accusam et justo duo dolores et ea rebum. Stet clita kasd gubergren, no sea takimata sanctus est Lorem ipsum dolor sit amet. Lorem ipsum dolor sit amet, consetetur sadipscing elitr, sed diam nonumy eirmod tempor invidunt ut labore et dolore magna aliquyam erat, sed diam voluptua. At vero eos et accusam et justo duo dolores et ea rebum. Stet clita kasd gubergren, no sea takimata sanctus est Lorem ipsum dolor sit amet. Lorem ipsum dolor sit amet, consetetur sadipscing elitr, sed diam nonumy eirmod tempor invidunt ut labore et dolore magna aliquyam erat, sed diam voluptua. At vero eos et accusam et justo duo dolores et ea rebum. Stet clita kasd gubergren, no sea takimata sanctus est Lorem ipsum dolor sit amet.</p>
    <p>Duis autem vel eum iriure dolor in <strong>hendrerit in vulputate</strong> velit esse molestie consequat, vel illum dolore eu feugiat nulla facilisis at vero eros et accumsan et iusto odio dignissim qui blandit praesent luptatum zzril delenit augue duis dolore te feugait nulla facilisi. Lorem ipsum dolor sit amet, consectetuer adipiscing elit, sed diam nonummy nibh euismod tincidunt ut laoreet dolore magna aliquam erat volutpat.</p>
    <p>Ut wisi enim ad minim veniam, quis nostrud exerci tation ullamcorper suscipit lobortis nisl ut aliquip ex ea commodo consequat. Duis autem vel eum iriure dolor in hendrerit in vulputate velit esse molestie consequat, vel illum dolore eu feugiat nulla facilisis at vero eros et accumsan et iusto odio dignissim qui blandit praesent luptatum zzril delenit augue duis dolore te feugait nulla facilisi. Nam liber tempor cum soluta nobis eleifend option congue nihil imperdiet doming id quod mazim placerat facer possim assum. Lorem ipsum dolor sit amet, consectetuer adipiscing elit.</p>
  </div>

  <h2 class="abs cv-heading">Lebenslauf</h2>
  <div class="abs timeline-line"></div>

  <div class="abs cv-item" style="top:424px">
    <div class="cv-icon"><svg width="8" height="8" viewBox="0 0 8 8"><rect x=".5" y="1.2" width="7" height="6.3" fill="none" stroke="#1f5a99" stroke-width=".8"/><line x1=".5" y1="3" x2="7.5" y2="3" stroke="#1f5a99" stroke-width=".8"/></svg></div>
    <div class="cv-date">Muster Datum</div>
    <div class="cv-desc">Muster Text Lorem ipsum dolor sit amet, consetetur sadipscing elitr, sed diam nonumy eirmod tempor invidunt ut labore et dolore magna aliquyam erat, sed diam voluptua.</div>
  </div>
  <div class="abs cv-item" style="top:479px">
    <div class="cv-icon"><svg width="8" height="8" viewBox="0 0 8 8"><rect x=".5" y="1.2" width="7" height="6.3" fill="none" stroke="#1f5a99" stroke-width=".8"/><line x1=".5" y1="3" x2="7.5" y2="3" stroke="#1f5a99" stroke-width=".8"/></svg></div>
    <div class="cv-date">Muster Datum</div>
    <div class="cv-desc">Muster Text Lorem ipsum dolor sit amet, consetetur sadipscing elitr, sed diam nonumy eirmod tempor invidunt ut labore et dolore magna aliquyam erat, sed diam voluptua.</div>
  </div>
  <div class="abs cv-item" style="top:535px">
    <div class="cv-icon"><svg width="8" height="8" viewBox="0 0 8 8"><rect x=".5" y="1.2" width="7" height="6.3" fill="none" stroke="#1f5a99" stroke-width=".8"/><line x1=".5" y1="3" x2="7.5" y2="3" stroke="#1f5a99" stroke-width=".8"/></svg></div>
    <div class="cv-date">Muster Datum</div>
    <div class="cv-desc">Muster Text Lorem ipsum dolor sit amet, consetetur sadipscing elitr, sed diam nonumy eirmod tempor invidunt ut labore et dolore magna aliquyam erat, sed diam voluptua.</div>
  </div>
  <div class="abs cv-item" style="top:590px">
    <div class="cv-icon"><svg width="8" height="8" viewBox="0 0 8 8"><rect x=".5" y="1.2" width="7" height="6.3" fill="none" stroke="#1f5a99" stroke-width=".8"/><line x1=".5" y1="3" x2="7.5" y2="3" stroke="#1f5a99" stroke-width=".8"/></svg></div>
    <div class="cv-date">Muster Datum</div>
    <div class="cv-desc">Muster Text Lorem ipsum dolor sit amet, consetetur sadipscing elitr, sed diam nonumy eirmod tempor invidunt ut labore et dolore magna aliquyam erat, sed diam voluptua.</div>
  </div>
  <div class="abs cv-item" style="top:645px">
    <div class="cv-icon"><svg width="8" height="8" viewBox="0 0 8 8"><rect x=".5" y="1.2" width="7" height="6.3" fill="none" stroke="#1f5a99" stroke-width=".8"/><line x1=".5" y1="3" x2="7.5" y2="3" stroke="#1f5a99" stroke-width=".8"/></svg></div>
    <div class="cv-date">Muster Datum</div>
    <div class="cv-desc">Muster Text Lorem ipsum dolor sit amet, consetetur sadipscing elitr, sed diam nonumy eirmod tempor invidunt ut labore et dolore magna aliquyam erat, sed diam voluptua.</div>
  </div>
  <div class="abs cv-item" style="top:700px">
    <div class="cv-icon"><svg width="8" height="8" viewBox="0 0 8 8"><rect x=".5" y="1.2" width="7" height="6.3" fill="none" stroke="#1f5a99" stroke-width=".8"/><line x1=".5" y1="3" x2="7.5" y2="3" stroke="#1f5a99" stroke-width=".8"/></svg></div>
    <div class="cv-date">Muster Datum</div>
    <div class="cv-desc">Muster Text Lorem ipsum dolor sit amet, consetetur sadipscing elitr, sed diam nonumy eirmod tempor invidunt ut labore et dolore magna aliquyam erat, sed diam voluptua.</div>
  </div>
  <div class="abs cv-item" style="top:763px">
    <div class="cv-icon"><svg width="8" height="8" viewBox="0 0 8 8"><rect x=".5" y="1.2" width="7" height="6.3" fill="none" stroke="#1f5a99" stroke-width=".8"/><line x1=".5" y1="3" x2="7.5" y2="3" stroke="#1f5a99" stroke-width=".8"/></svg></div>
    <div class="cv-date">Muster Datum</div>
    <div class="cv-desc">Muster Text Lorem ipsum dolor sit amet, consetetur sadipscing elitr, sed diam nonumy eirmod tempor invidunt ut labore et dolore magna aliquyam erat, sed diam voluptua.</div>
  </div>

  <div class="abs text side-text-top">
    <p>Muster Text Lorem ipsum dolor sit amet, consetetur sadipscing elitr, sed diam nonumy eirmod tempor invidunt ut labore et dolore magna aliquyam erat, sed diam voluptua. At vero eos et accusam et justo duo dolores et ea rebum. Stet clita kasd gubergren, no sea takimata sanctus est Lorem ipsum dolor sit amet. Lorem ipsum dolor sit amet.</p>
    <p>Consetetur sadipscing elitr, sed diam nonumy eirmod tempor invidunt ut labore et dolore magna aliquyam erat, sed diam voluptua. At vero eos et accusam et justo duo <strong>dolores et ea rebum</strong>. Stet clita kasd gubergren, no sea takimata sanctus est Lorem ipsum dolor sit amet. Lorem ipsum dolor sit amet, consetetur sadipscing elitr, sed diam nonumy eirmod tempor invidunt ut labore et dolore.</p>
  </div>

  <div class="abs slider" role="img" aria-label="Entspannte Rückenmassage in der Praxis">
    <div class="dots"><span></span><span class="active"></span><span></span><span></span></div>
  </div>

  <div class="abs text side-text-bottom">
    <p>Consetetur sadipscing elitr, sed diam nonumy eirmod tempor invidunt ut labore et dolore magna aliquyam erat, sed diam voluptua. At vero eos et accusam et justo duo dolores et ea rebum. Stet clita kasd gubergren, no sea takimata sanctus est Lorem ipsum dolor sit amet. rebum. Stet clita kasd gubergren, no sea takimata sanctus est Lorem ipsum dolor sit amet. Lorem ipsum dolor sit amet, <strong>consetetur sadipscing elitr</strong>, sed diam nonumy eirmod tempor invidunt ut labore et dolore.</p>
    <p>Aliquyam erat, sed diam voluptua. At vero eos et accusam et justo duo dolores et ea rebum. Stet clita kasd gubergren, no sea takimata sanctus est Lorem ipsum dolor sit amet.</p>
  </div>

  <section>
    <div class="abs band"></div>
    <div class="abs band-mark"><span>LUMENSTILLE</span></div>
    <div class="abs text band-text">
      <p class="lead">Muster Text Lorem ipsum dolor sit amet consetetur.</p>
      <p>Lorem ipsum dolor sit amet, consetetur sadipscing elitr, sed diam nonumy eirmod tempor invidunt ut labore.<br>Et dolore magna aliquyam erat, sed diam voluptua. At vero eos et accusam et justo duo dolores et ea rebum Stet clita kasd gubergren, no sea takimata sanctus est Lorem ipsum dolor sit amet. Lorem ipsum dolor sit amet, consetetur sadipscing elitr, sed diam nonumy eirmod tempor invidunt ut labore.</p>
    </div>
    <div class="abs cta">
      <svg width="6" height="5" viewBox="0 0 6 5" aria-hidden="true"><path d="M3.5 .5 L5.5 2.2 L3.5 4 M5.5 2.2 H2.5 Q.5 2.2 .5 4.5" fill="none" stroke="#fff" stroke-width=".7"/></svg>
      JETZT KONTAKT AUFNEHMEN
    </div>
  </section>
</main>

<footer>
  <div class="abs footer"></div>
  <div class="abs footer-brand">LUMENSTILLE</div>
  <div class="abs social" aria-label="Soziale Netzwerke"><span></span><span></span><span></span><span></span><span></span></div>
  <div class="abs copyright">© 2018 LUMENSTILLE. Alle Rechte vorbehalten</div>
  <div class="abs to-top">
    <svg width="6" height="4" viewBox="0 0 6 4" aria-hidden="true"><path d="M.5 3.5 L3 1 L5.5 3.5" fill="none" stroke="#fff" stroke-width="1"/></svg>
  </div>
</footer>

</body>
</html>
```